Need a simple buisness card for my plumbing business. Would like it to be black background with white text.

Industry/Entity Type

Business

Requirements
Must have
• On the front of the card I need to have,
TKB PLUMBING SERVICES
PLUMBERS, DRAINERS & GASFITTERS
Dorian Wellsby
0471596083
Info@tkbplumbingservices.com.au
LIC No 517483f
ABN No 61907354218
On the back I need in point form
Domestic,industrial,commercial, all new installations, renovations, sewer renewals, repairs,
Fully licensed and insured
Nice to have
• A nice simple logo

```html
<!DOCTYPE html>
<html lang="en">
<head>
<meta charset="utf-8">
<title>TKB Plumbing Services – Business Card</title>
<link rel="stylesheet" href="https://fonts.googleapis.com/css2?family=Arimo:wght@400;700&display=swap">
<style>
  :root {
    --backdrop: #8c8c8c;
    --card-core: #2a2a2a;
    --card-edge: #030303;
    --ink: #e4e4e4;
    --ink-soft: #c9c9c9;
    --rule: #f2f2f2;
    --trade-bg: #1a1a1a;
  }
  * { box-sizing: border-box; margin: 0; padding: 0; }
  html, body {
    width: 1200px; height: 1200px; overflow: hidden;
    background: var(--backdrop);
    font-family: "Arimo", Arial, sans-serif;
  }
  .card {
    position: absolute; left: 206px; width: 760px; height: 452px;
    background: radial-gradient(ellipse 70% 75% at 50% 50%, var(--card-core), var(--card-edge));
    color: var(--ink); overflow: hidden;
  }
  .card--front { top: 89px; }
  .card--back { top: 617px; }

  .brand-mark { position: absolute; left: 340px; top: 22px; width: 76px; height: 76px; }
  .rule { position: absolute; height: 3px; background: var(--rule); }
  .rule--upper-left { left: 0; top: 186px; width: 186px; }
  .rule--upper-right { left: 578px; top: 186px; width: 182px; }
  .rule--lower { left: 0; top: 273px; width: 760px; }
  .brand-name {
    position: absolute; left: 0; right: 0; top: 111px; text-align: center;
    font-size: 125px; font-weight: 400; line-height: 1; letter-spacing: 12px;
    padding-left: 12px; color: var(--ink);
  }
  .brand-sub {
    position: absolute; left: 0; right: 0; top: 222px; text-align: center;
    font-weight: 700; line-height: 1; color: var(--ink); white-space: nowrap;
  }
  .brand-sub__lead { font-size: 30px; }
  .brand-sub__tail { font-size: 24px; }
  .trade-line {
    position: absolute; left: 50%; top: 266px; transform: translateX(-50%);
    padding: 0 6px; background: var(--trade-bg);
    font-size: 11px; font-weight: 700; letter-spacing: 0.3px; color: var(--ink-soft);
    white-space: nowrap; line-height: 17px;
  }
  .contact { position: absolute; font-size: 21px; font-weight: 700; color: var(--ink-soft); white-space: nowrap; line-height: 1; }
  .contact--name { left: 124px; top: 328px; }
  .contact--phone { left: 436px; top: 328px; letter-spacing: 1px; }
  .contact--email { left: 127px; top: 362px; font-weight: 400; font-size: 21px; }
  .registration {
    position: absolute; right: 38px; top: 410px; font-size: 16px; font-weight: 700; line-height: 1;
    color: var(--ink-soft); white-space: nowrap; word-spacing: 2px;
  }
  .registration span + span { margin-left: 14px; }

  .service-list { list-style: none; }
  .service {
    position: absolute; font-size: 17px; font-weight: 700; line-height: 1;
    color: var(--ink-soft); white-space: nowrap; letter-spacing: 0.5px;
  }
  .service:nth-child(1) { left: 124px; top: 92px; }
  .service:nth-child(2) { left: 180px; top: 114px; }
  .service:nth-child(3) { left: 233px; top: 136px; }
  .service:nth-child(4) { left: 298px; top: 158px; }
  .service:nth-child(5) { left: 362px; top: 178px; }
  .service:nth-child(6) { left: 416px; top: 199px; }
  .service:nth-child(7) { left: 474px; top: 219px; }
  .assurance {
    position: absolute; left: 118px; top: 364px; font-size: 25px; font-weight: 700;
    color: var(--ink); white-space: nowrap;
  }
</style>
</head>
<body>
  <section class="card card--front" aria-label="Card front">
    <svg class="brand-mark" viewBox="0 0 76 76" aria-hidden="true">
      <circle cx="38" cy="38" r="34" fill="var(--ink)"/>
    </svg>
    <div class="rule rule--upper-left"></div>
    <div class="rule rule--upper-right"></div>
    <h1 class="brand-name">TKB</h1>
    <p class="brand-sub"><span class="brand-sub__lead">PLUMBING</span> <span class="brand-sub__tail">SERVICES</span></p>
    <div class="rule rule--lower"></div>
    <p class="trade-line">PLUMBERS, DRAINERS &amp; GASFITTERS</p>
    <p class="contact contact--name">DORIAN WELLSBY</p>
    <p class="contact contact--phone">0471596083</p>
    <p class="contact contact--email">Info@tkbplumbingservices.com.au</p>
    <p class="registration"><span>ABN Nº 61907354218</span><span>LIC Nº 517483F</span></p>
  </section>

  <section class="card card--back" aria-label="Card back">
    <ul class="service-list">
      <li class="service">DOMESTIC</li>
      <li class="service">INDUSTRIAL</li>
      <li class="service">COMMERCIAL</li>
      <li class="service">ALL NEW RENOVATIONS</li>
      <li class="service">RENOVATIONS</li>
      <li class="service">SEWER RENEWALS</li>
      <li class="service">REPAIRS</li>
    </ul>
    <p class="assurance">FULLY LICENSED AND INSURED</p>
  </section>
</body>
</html>
```